Flyer for the Radiant Harvest Worship Day 2020

I am looking to create a flyer for a one day prayer retreat our church is organizing.
This flyer will be posted on social media, websites and will also be printed so it can be mailed to people.
I am looking for something professional, with good use of our logo and band colors (logo colors).
I am counting on the designer's skill, creativity, art and knowledge of media communication to produce a flyer that will effectively and quickly convey the message we are trying to spread.
CONTENT OF THE FLYER:
Event title: Radiant Harvest Worship Day
Date: Tuesday July 2nd, 2020
Time: 11:00AM - 7:00PM
Belmora Hotel, 4876 Willowmere Street, Portland, Maine 04987 (Room: Evergrove)
Event Key words to highlight what the event is about: Prayer, Sharing the Word, Panel discussion, prophecy, Impartation.
Key phrases:
A one day prayer retreat.
Jesus Chris is Lord
Contact info:
www.toluvek.org
Phone: 207 555 0183
Email: contact@brightmeadowfold.org

```html
<!DOCTYPE html>
<html lang="en">
<head>
<meta charset="utf-8">
<title>Radiant Harvest Worship Day 2020</title>
<link href="https://fonts.googleapis.com/css2?family=Kaushan+Script&family=Montserrat:wght@500;600;700;800&display=swap" rel="stylesheet">
<style>
  :root {
    --page: #ffffff;
    --orange: #f29222;
    --orange-deep: #e2571f;
    --navy: #0b2a4a;
    --ink: #1b1b1d;
    --white: #ffffff;
    --box-text: #2a1a0c;
  }
  * { margin: 0; padding: 0; box-sizing: border-box; }
  html, body { width: 1200px; height: 912px; overflow: hidden; background: var(--page); }
  .canvas { position: relative; width: 1200px; height: 912px; }
  .flyer {
    position: absolute; left: 297px; top: 63px; width: 611px; height: 791px;
    background: linear-gradient(180deg, var(--ink) 0%, var(--ink) 52%, #14202e 72%, var(--navy) 100%);
    overflow: hidden;
    font-family: "Montserrat", sans-serif;
  }
  .hero-photo {
    position: absolute; left: 0; top: 0; width: 611px; height: 374px;
    background: linear-gradient(180deg, #a9aeb3 0%, #bcb2a3 22%, #988a80 45%, #4e4442 70%, #0b0a0b 100%);
  }
  .frame-top { position: absolute; left: 17px; top: 22px; width: 577px; height: 3px; background: var(--orange); }
  .frame-side {
    position: absolute; top: 22px; width: 3px; height: 717px;
    background: linear-gradient(180deg, var(--orange) 0%, var(--orange) 60%, rgba(242,146,34,0) 100%);
  }
  .frame-side.left { left: 17px; }
  .frame-side.right { left: 591px; }
  .title-main {
    position: absolute; left: 0; width: 611px; top: 268px; text-align: center;
    font-family: "Kaushan Script", cursive; font-size: 98px; line-height: 1; white-space: nowrap;
    background: linear-gradient(180deg, var(--orange) 25%, var(--orange-deep) 100%);
    -webkit-background-clip: text; background-clip: text; color: transparent;
  }
  .title-sub {
    position: absolute; left: 0; width: 611px; top: 256px; text-align: center; z-index: 2;
    font-family: "Kaushan Script", cursive; font-size: 40px; color: #f1f1f1; line-height: 1;
  }
  .tagline {
    position: absolute; left: 0; width: 611px; top: 392px; text-align: center;
    color: var(--white); font-size: 17px; font-weight: 500; letter-spacing: 3px;
  }
  .motto {
    position: absolute; left: 0; width: 611px; top: 410px; text-align: center;
    color: var(--white); font-size: 34px; font-weight: 500; letter-spacing: 3px;
  }
  .when {
    position: absolute; right: 323px; top: 497px; text-align: right; line-height: 1;
    font-weight: 800;
  }
  .when .day { color: var(--orange); font-size: 31px; }
  .when .date { color: var(--orange); font-size: 19px; margin-top: 8px; }
  .when .time { color: var(--white); font-size: 17px; margin-top: 9px; }
  .divider { position: absolute; left: 305px; top: 495px; width: 2px; height: 86px; background: var(--white); }
  .where {
    position: absolute; left: 322px; top: 500px; color: var(--orange);
    font-size: 14px; font-weight: 700; line-height: 19px;
  }
  .highlights {
    position: absolute; left: 44px; top: 596px; width: 524px; height: 81px;
    background: var(--orange); color: var(--box-text);
    display: flex; flex-direction: column; justify-content: center; align-items: center;
    font-size: 16px; font-weight: 500; line-height: 25px; letter-spacing: .2px;
  }
  .brand {
    position: absolute; left: 80px; top: 706px; display: flex; align-items: center; gap: 7px;
    color: var(--white); font-size: 24px; font-weight: 600;
  }
  .brand .dot { width: 11px; height: 11px; border-radius: 50%; background: var(--orange); }
  .contact {
    position: absolute; left: 240px; width: 306px; top: 703px; text-align: center;
    color: var(--white); font-size: 19px; font-weight: 800; white-space: nowrap;
  }
  .contact-links {
    position: absolute; left: 241px; top: 734px; display: flex; align-items: center; gap: 6px;
    color: var(--white); font-size: 10px; font-weight: 700; white-space: nowrap;
  }
  .contact-links svg { flex: none; }
  .contact-links .gap { width: 8px; }
</style>
</head>
<body>
<div class="canvas">
  <div class="flyer">
    <div class="hero-photo" role="img" aria-label="Photo: silhouette of a man praying with clasped hands above a misty mountain landscape at sunrise"></div>
    <div class="frame-top"></div>
    <div class="frame-side left"></div>
    <div class="frame-side right"></div>

    <div class="title-main">Worship Day</div>
    <div class="title-sub">Radiant Harvest</div>

    <div class="tagline">A ONE DAY PRAYER RETREAT</div>
    <div class="motto">Jesus Chris is Lord</div>

    <div class="when">
      <div class="day">TUESDAY</div>
      <div class="date">JULY 2ND, 2020</div>
      <div class="time">11:00AM - 7:00PM</div>
    </div>
    <div class="divider"></div>
    <div class="where">
      Belmora Hotel<br>
      4876 Willowmere Street,<br>
      Portland, Maine 04987<br>
      (Room: Evergrove)
    </div>

    <div class="highlights">
      <div>&bull; PRAYER &bull; SHARING THE WORD &bull; PANEL DISCUSSION</div>
      <div>&bull; PROPHECY &bull; IMPARTATION</div>
    </div>

    <div class="brand"><span class="dot"></span>Toluvek</div>

    <div class="contact">CONTACT US: 207 555 0183</div>
    <div class="contact-links">
      <svg width="25" height="18" viewBox="0 0 25 18" aria-hidden="true">
        <rect x="1" y="1" width="23" height="16" fill="none" stroke="#fff" stroke-width="1.5"/>
        <polyline points="1,1 12.5,10 24,1" fill="none" stroke="#fff" stroke-width="1.5"/>
        <line x1="1" y1="17" x2="9" y2="8" stroke="#fff" stroke-width="1.2"/>
        <line x1="24" y1="17" x2="16" y2="8" stroke="#fff" stroke-width="1.2"/>
      </svg>
      <span>contact@brightmeadowfold.org</span>
      <span class="gap"></span>
      <svg width="22" height="22" viewBox="0 0 22 22" aria-hidden="true">
        <circle cx="11" cy="11" r="10" fill="none" stroke="#fff" stroke-width="1.4"/>
        <ellipse cx="11" cy="11" rx="4.5" ry="10" fill="none" stroke="#fff" stroke-width="1.2"/>
        <line x1="1" y1="11" x2="21" y2="11" stroke="#fff" stroke-width="1.2"/>
        <line x1="3" y1="6" x2="19" y2="6" stroke="#fff" stroke-width="1"/>
        <line x1="3" y1="16" x2="19" y2="16" stroke="#fff" stroke-width="1"/>
      </svg>
      <span>www.toluvek.org</span>
    </div>
  </div>
</div>
</body>
</html>
```